International Food Manufacturer in the need of a new business card and logo.

Our Company - Northgate Pantry Ltd.

Our Industry - Food and Drink

We are a Wild Harvested Food Distributor / Manufacturer. We service the following food sectors: Supermarkets, Hotels, Restaurants, Cafes, Catering and all people looking to eat healthy food products.

Slogan - The foremost source for everything healthy

Business card details -

48-52 Marlow Lane
Hatherby Green
London
EC9Z 4RT United Kingdom
Dennis Prowle
+44 7000 481736 - UK
+971 50 7739205 - UAE
+38 063 914 2758 - Ukraine
dennis@northgatepantry.example
www.northgatepantry.example

Goal - We are looking for a dynamic modern new look for our corporate image and a designer who can bring this new concept to our future food product designs. Please try to incorporate 3d hexagonal vector Imaging in your design concepts.

Target Market(s)

Industry/Entity Type

Food Service

Contact Information for Business Card

Northgate Pantry Ltd.
48-52 Marlow Lane
Hatherby Green
London
EC9Z 4RT United Kingdom
Dennis Prowle
+44 7000 481736 - UK
+971 50 7739205 - UAE

Font styles to use
Serif

Colors

Designer to choose colors to be used in the design.

Requirements
Must have
• Please read project description above.
Nice to have
Should not have

```html
<!DOCTYPE html>
<html lang="en">
<head>
<meta charset="utf-8">
<title>Northgate Pantry Ltd. — Business Card</title>
<link rel="stylesheet" href="https://fonts.googleapis.com/css2?family=Roboto:wght@300;400;900&display=swap">
<style>
  :root {
    --page: #e4e4e4;
    --card: #232323;
    --band-light: #f1f2f5;
    --band-mid: #d9dbe0;
    --accent: #1b86bf;
    --text: #ffffff;
  }
  html, body {
    margin: 0;
    width: 1200px;
    height: 1200px;
    overflow: hidden;
    background: var(--page);
    font-family: "Roboto", Arial, sans-serif;
  }
  .card {
    position: absolute;
    left: 100px;
    top: 314px;
    width: 1000px;
    height: 572px;
    background: var(--card);
    color: var(--text);
    overflow: hidden;
    box-shadow: 0 10px 30px rgba(0,0,0,0.18);
  }
  .hex-band {
    position: absolute;
    left: 0;
    top: 160px;
    width: 100%;
    height: 190px;
    background: radial-gradient(ellipse at 55% 60%, var(--band-mid), var(--band-light) 70%);
  }
  .name {
    position: absolute;
    left: 44px;
    top: 38px;
    margin: 0;
    font-weight: 900;
    font-size: 68px;
    letter-spacing: 1px;
    text-transform: uppercase;
  }
  .slogan {
    position: absolute;
    left: 44px;
    top: 118px;
    margin: 0;
    font-weight: 300;
    font-size: 27px;
    letter-spacing: 0.5px;
  }
  .brand {
    position: absolute;
    right: 36px;
    top: 112px;
    display: flex;
    align-items: center;
    gap: 14px;
    font-weight: 400;
    font-size: 27px;
  }
  .brand-mark {
    width: 26px;
    height: 26px;
    background: var(--accent);
  }
  .row {
    position: absolute;
    left: 28px;
    display: flex;
    align-items: center;
    gap: 10px;
    font-size: 24px;
    white-space: nowrap;
  }
  .icon {
    width: 38px;
    height: 38px;
    background: var(--accent);
    display: flex;
    align-items: center;
    justify-content: center;
    flex: none;
  }
  .icon svg { width: 20px; height: 20px; fill: #fff; }
  .num {
    background: var(--accent);
    padding: 4px 6px;
  }
  .phones { top: 340px; }
  .address { top: 392px; }
  .web { top: 444px; }
  .email { top: 480px; left: 470px; }
</style>
</head>
<body>
  <article class="card">
    <div class="hex-band" role="img" aria-label="Light grey band of raised 3D hexagon tiles"></div>

    <h1 class="name">Dennis Prowle</h1>
    <p class="slogan">The foremost source for everything healthy</p>

    <div class="brand">
      <span class="brand-mark"></span>
      <span class="brand-name">Northgate Pantry Ltd.</span>
    </div>

    <div class="row phones">
      <span class="icon"><svg viewBox="0 0 24 24"><path d="M6.6 10.8a15.1 15.1 0 0 0 6.6 6.6l2.2-2.2a1 1 0 0 1 1-.25 11.4 11.4 0 0 0 3.6.57 1 1 0 0 1 1 1V20a1 1 0 0 1-1 1A17 17 0 0 1 3 4a1 1 0 0 1 1-1h3.5a1 1 0 0 1 1 1c0 1.25.2 2.45.57 3.57a1 1 0 0 1-.25 1z"/></svg></span>
      <span>UK</span><span class="num">+44 7000 481736</span>
      <span>UAE</span><span class="num">+971 50 7739205</span>
      <span>Ukraine</span><span class="num">+38 063 914 2758</span>
    </div>

    <div class="row address">
      <span class="icon"><svg viewBox="0 0 24 24"><path d="M12 2a7 7 0 0 0-7 7c0 5.2 7 13 7 13s7-7.8 7-13a7 7 0 0 0-7-7zm0 9.5A2.5 2.5 0 1 1 12 6.5a2.5 2.5 0 0 1 0 5z"/></svg></span>
      <span>48-52 Marlow Lane, Hatherby Green, London, EC9Z 4RT United Kingdom</span>
    </div>

    <div class="row web">
      <span class="icon"><svg viewBox="0 0 24 24"><path d="M12 2a10 10 0 1 0 0 20 10 10 0 0 0 0-20zm6.9 6h-3a15.6 15.6 0 0 0-1.4-3.6A8 8 0 0 1 18.9 8zM12 4c.8 1.2 1.5 2.5 1.9 4h-3.8c.4-1.5 1.1-2.8 1.9-4zM4.3 14a8.2 8.2 0 0 1 0-4h3.4a16.5 16.5 0 0 0 0 4zm.8 2h3a15.6 15.6 0 0 0 1.4 3.6A8 8 0 0 1 5.1 16zm3-8h-3a8 8 0 0 1 4.4-3.6A15.6 15.6 0 0 0 8.1 8zM12 20c-.8-1.2-1.5-2.5-1.9-4h3.8c-.4 1.5-1.1 2.8-1.9 4zm2.3-6H9.7a14.7 14.7 0 0 1 0-4h4.6a14.7 14.7 0 0 1 0 4zm.2 5.6a15.6 15.6 0 0 0 1.4-3.6h3a8 8 0 0 1-4.4 3.6zm1.8-5.6a16.5 16.5 0 0 0 0-4h3.4a8.2 8.2 0 0 1 0 4z"/></svg></span>
      <span>www.northgatepantry.example</span>
    </div>

    <div class="row email">
      <span class="icon"><svg viewBox="0 0 24 24"><path d="M3 5h18v14H3zm2 2v.5l7 4.5 7-4.5V7zm0 2.9V17h14V9.9l-7 4.5z"/></svg></span>
      <span>dennis@northgatepantry.example</span>
    </div>
  </article>
</body>
</html>
```